Lone Star Wetland Flora Stewardship Guild

We need to design the home page of this new website. We would like a fun website design for provides as a resource for members and information for potential members.
Please design so that we can see a portion of background on each side on the website.
I just need the final design files psd no coding needed.
Attached is their logo (colors are not 100% set in stone either so can mess with those as I did in the quick mockup attached)
Attached is a pdf newsletter they send out, you can get a feel for them and what they are about. The design is crappy and we are here to fix that going forward and we are starting with the website.
Here are some quick example websites (design style is open)
- I attached a quick mockup i did just for a content visual but by all means do what you want.
- http://www.brindlecourtleaders.org/
- http://www.qvelto.org/
- http://preview.plimworks7.com/view.php?cat=layoutpacks&host=gridcrafthub&temp=venrolite
- http://www.ploughvale.org/
- http://www.townmarrow.org/
- http://www.projectkindlecoat.org/
here are some of the other chapters website (pretty bad!)
and here are some of the others:
- http://www.zrelkq.org/
- http://ovtu.org/
- http://www.lirvx.org/
Content Items that need to be included:
1. Logo
2. Menu - home, about, members, resources, events, membership, contact
3. Become a member - button or action
4. social links - friendwall, jobrungo, clipzora
5. banner - that needs to explain their purpose "Promoting environmental stewardship through operations, research, education and outreach" (or this can be worked into the design)
6. Upcoming event (s)
7. Advertisement - members can place an ad on the website, this can be a placeholder for now
8. newsletter signup
9. advertise with us - this link can be in the footer
30-60 years of age, succesfull (household budgets of 120K+ men and women that live in texas.
Education

```html
<!DOCTYPE html>
<html lang="en">
<head>
<meta charset="utf-8">
<title>Lone Star Wetland Flora Stewardship Guild</title>
<link href="https://fonts.googleapis.com/css2?family=Open+Sans:wght@300;400;600;700&display=swap" rel="stylesheet">
<style>
:root{
  --navy:#0b2674;
  --navy-deep:#08205f;
  --orange:#e2680c;
  --sky:#0a86bf;
  --event-blue:#1898d4;
  --red:#c3161c;
  --link:#15307f;
  --text:#2b2b2b;
  --muted:#555;
  --rule:#d8d8d8;
  --gray-bg:#f3f3f3;
  --field:#4863a8;
}
*{box-sizing:border-box;margin:0;padding:0}
html,body{width:815px;height:1200px;overflow:hidden}
body{font-family:"Open Sans",Arial,sans-serif;color:var(--text);background:#fff;position:relative}
.wrap{width:638px;margin:0 auto;position:relative}
a{color:inherit;text-decoration:none}

/* header */
.site-header{height:73px}
.brand{position:absolute;left:0;top:18px;display:flex;align-items:center;gap:10px}
.brand-mark{width:30px;height:30px;background:var(--navy)}
.brand-name{font-weight:700;font-size:11.5px;line-height:14px;color:var(--navy-deep);width:190px;text-transform:uppercase}
.utility{position:absolute;right:4px;top:6px;display:flex;gap:18px;font-size:10px;color:#333;align-items:center}
.utility span{display:flex;align-items:center;gap:6px}
.utility .sep{width:1px;height:12px;background:#bbb}
.join-btn{position:absolute;right:0;top:28px;width:226px;height:33px;background:var(--orange);color:#fff;display:flex;align-items:center;font-size:14px;font-weight:300;letter-spacing:.2px}
.join-icon{width:38px;height:33px;background:#fff;clip-path:polygon(0 0,70% 0,100% 50%,70% 100%,0 100%);display:flex;align-items:center;justify-content:center;margin-right:10px}

/* nav */
.main-nav{background:var(--navy);height:34px}
.main-nav ul{list-style:none;display:flex;height:34px}
.main-nav li{font-size:10.5px;color:#fff;text-transform:uppercase;display:flex;align-items:center;justify-content:center}
.main-nav li.active{background:var(--orange)}

/* hero */
.hero{background:var(--sky);height:254px}
.hero .wrap{height:254px}
.hero-photo{position:absolute;inset:0;background:linear-gradient(180deg,#8fb6d0 0%,#b9cfd8 22%,#6a8c3c 30%,#7c9a48 44%,#4f7290 58%,#5b84a6 100%)}
.hero-arrow{position:absolute;top:102px;width:29px;height:29px;background:#d7e6ee;display:flex;align-items:center;justify-content:center}
.hero-arrow.prev{left:0}.hero-arrow.next{right:0}
.hero-caption{position:absolute;left:0;right:0;bottom:0;height:77px;background:rgba(20,60,80,.45);color:#fff;text-align:center;font-weight:300;font-size:18px;line-height:21px;padding-top:6px}
.dots{position:absolute;left:0;right:0;bottom:5px;display:flex;justify-content:center;gap:5px}
.dots i{width:10px;height:10px;border-radius:50%;border:1.5px solid #fff}
.dots i.on{background:#fff}

/* about & events */
.intro{height:305px;position:relative}
.col-left{position:absolute;left:0;top:18px;width:309px}
.col-right{position:absolute;left:329px;top:18px;width:309px}
.section-head{display:flex;justify-content:space-between;align-items:center;border-bottom:1px solid var(--rule);padding-bottom:4px;height:30px}
.section-head h2{font-weight:300;font-size:22px;color:var(--red)}
.btn{background:var(--sky);color:#fff;font-size:10px;font-weight:600;height:22px;padding:0 14px;display:flex;align-items:center}
.about-text{font-size:10.6px;line-height:16px;text-align:justify;margin-top:16px;height:230px;overflow:hidden}
.about-text p+p{margin-top:16px}
.event{display:flex;height:63px;border:1px solid var(--rule);margin-top:16px}
.event:first-of-type{margin-top:13px}
.event-date{width:59px;background:var(--event-blue);color:#fff;text-align:center;position:relative;padding-top:9px;font-weight:300;font-size:17px;line-height:19px}
.event-date b{display:block;font-weight:600;font-size:18px}
.event-date::after{content:"";position:absolute;right:-8px;top:22px;border-left:8px solid var(--event-blue);border-top:8px solid transparent;border-bottom:8px solid transparent}
.event-body{padding:6px 8px 0 20px}
.event-body h3{font-size:11.5px;font-weight:400;color:var(--link);line-height:13px}
.event-body p{font-size:8.5px;color:#333;margin-top:3px}

/* news */
.lower{background:var(--gray-bg);height:320px;border-top:1px solid #e2e2e2}
.news{position:absolute;left:0;top:22px;width:419px}
.news-list{background:#fff;margin-top:13px}
.news-item{display:flex;align-items:center;border-bottom:1px solid #e6e6e6;padding:0 6px}
.news-item:first-child{height:54px}
.news-item{height:63px}
.news-item:last-child{border-bottom:none}
.thumb{width:52px;height:42px;flex:none}
.thumb.lodge{background:#e9e9e9}
.thumb.pond{background:linear-gradient(160deg,#7ea04a,#4d7a3a 60%,#6d93b0)}
.news-text{padding-left:22px}
.news-text h3{font-size:11.5px;font-weight:400;color:var(--link);line-height:13px}
.news-text p{font-size:8.5px;color:#333;margin-top:3px}
.ad{position:absolute;left:438px;top:21px;width:200px;height:258px}
.ad-photo{height:203px;background:linear-gradient(180deg,#1b85b8,#0f5e8f 60%,#1a3d5a)}
.ad-brand{height:55px;background:#dedede;display:flex;align-items:center;justify-content:center;font-size:15px;font-weight:600;color:var(--navy-deep)}

/* footer */
.site-footer{background:var(--navy);height:178px;color:#fff}
.site-footer .wrap{height:178px}
.quick{position:absolute;left:1px;top:22px}
.site-footer h4{font-size:11px;font-weight:600;margin-bottom:10px}
.quick ul{list-style:none;font-size:10px;line-height:15px}
.signup{position:absolute;left:166px;top:22px;width:254px}
.signup p{font-size:10px;line-height:12px;padding-bottom:10px;border-bottom:1px solid #3a55a0}
.fields{display:flex;flex-wrap:wrap;gap:6px;margin-top:7px}
.field{height:23px;background:var(--field);font-size:9.5px;color:#dfe6f5;padding:5px 6px}
.field.half{width:124px}.field.email{width:208px}
.submit{width:44px;height:23px;background:#fff;display:flex;align-items:center;justify-content:center}
.follow{position:absolute;left:494px;top:22px}
.socials{display:flex;gap:7px}
.socials i{width:20px;height:20px;border:1px solid #5a72b4;background:#1c3a8c}
.copyright{background:var(--navy-deep);height:36px;border-top:1px solid #2a4596;color:#fff;font-size:8.5px;text-align:center;line-height:34px}
</style>
</head>
<body>

<header class="site-header">
  <div class="wrap">
    <div class="brand"><span class="brand-mark"></span><span class="brand-name">Lone Star Wetland Flora Stewardship Guild</span></div>
    <div class="utility">
      <span><svg width="11" height="8" viewBox="0 0 11 8"><rect x=".5" y=".5" width="10" height="7" fill="none" stroke="#333"/><path d="M.5 .5 5.5 4.5 10.5 .5" fill="none" stroke="#333"/></svg>CONTACT</span>
      <i class="sep"></i>
      <span><svg width="9" height="10" viewBox="0 0 9 10"><circle cx="4.5" cy="2.7" r="2.4" fill="#333"/><path d="M0 10a4.5 4 0 0 1 9 0z" fill="#333"/></svg>LOGIN</span>
    </div>
    <a class="join-btn" href="#">
      <span class="join-icon"><svg width="20" height="14" viewBox="0 0 20 14"><circle cx="10" cy="4" r="3" fill="#0b2674"/><circle cx="4" cy="5" r="2.2" fill="#0b2674"/><circle cx="16" cy="5" r="2.2" fill="#0b2674"/><path d="M4 14a6 6 0 0 1 12 0zM0 13a4 4 0 0 1 6-3.4L5 13zM20 13a4 4 0 0 0-6-3.4l1 3.4z" fill="#0b2674"/></svg></span>
      ☆ BECOME A MEMBER ☆
    </a>
  </div>
</header>

<nav class="main-nav">
  <div class="wrap">
    <ul>
      <li class="active" style="width:70px">Home</li>
      <li style="width:82px">About</li>
      <li style="width:84px">Members</li>
      <li style="width:92px">Resources</li>
      <li style="width:86px">Events</li>
      <li style="width:113px">Membership</li>
      <li style="width:84px">Contact</li>
    </ul>
  </div>
</nav>

<section class="hero">
  <div class="wrap">
    <div class="hero-photo" role="img" aria-label="Photograph of a green wetland marsh with open water under a pale sky"></div>
    <span class="hero-arrow prev"><svg width="8" height="12" viewBox="0 0 8 12"><path d="M7 1 2 6l5 5" fill="none" stroke="#0b2674" stroke-width="2"/></svg></span>
    <span class="hero-arrow next"><svg width="8" height="12" viewBox="0 0 8 12"><path d="M1 1l5 5-5 5" fill="none" stroke="#0b2674" stroke-width="2"/></svg></span>
    <div class="hero-caption">Promoting Environmental Stewardship through<br>Operations, Research, Education and Outreach</div>
    <div class="dots"><i class="on"></i><i></i><i></i><i></i></div>
  </div>
</section>

<section class="intro wrap">
  <div class="col-left">
    <div class="section-head"><h2>About LSWFSG</h2><a class="btn" href="#">Read More</a></div>
    <div class="about-text">
      <p>The Lone Star Wetland Flora Stewardship Guild, Inc. is an organization of scientists, educators, students, commercial pesticide applicators, administrators, and concerned individuals interested in the management and study of aquatic plants. The membership reflects a diversity of federal, state, and local agencies; universities and colleges around the world; corporations; and small businesses.</p>
      <p>The Lone Star Wetland Flora Stewardship Guild, Inc. is an organization of scientists, educators, students, commercial pesticide applicators, administrators, and concerned individuals interested in the management and study of aquatic plants. The membership reflects a diversity of federal, state, and local agencies; universities and colleges around the world; corporations; and small businesses.</p>
    </div>
  </div>
  <div class="col-right">
    <div class="section-head"><h2>Upcoming Events</h2><a class="btn" href="#">View All</a></div>
    <div class="event"><div class="event-date">Aug<b>22</b></div><div class="event-body"><h3>Biology and Management of Spider Mites in Soybean</h3><p>Mirela Konwatt, Prairie Ridge State University</p></div></div>
    <div class="event"><div class="event-date">Aug<b>25</b></div><div class="event-body"><h3>Identification and Management of the Invasive 'Kudzu Bug' (Megacopta cribraria)</h3><p>Deron Halbrick, Aldenmoor University</p></div></div>
    <div class="event"><div class="event-date">Oct<b>22</b></div><div class="event-body"><h3>Fungicide Resistance: A Case Study QoI Resistant Rhizoctonia solani</h3><p>Mirela Konwatt, Prairie Ridge State University</p></div></div>
  </div>
</section>

<section class="lower">
  <div class="wrap">
    <div class="news">
      <div class="section-head"><h2>Latest News</h2><a class="btn" href="#">View All</a></div>
      <div class="news-list">
        <div class="news-item"><div class="thumb lodge" role="img" aria-label="Sponsor lodge emblem"></div><div class="news-text"><h3>2014 Sponsorship Brochure</h3><p>Mirela Konwatt, Prairie Ridge State University</p></div></div>
        <div class="news-item"><div class="thumb pond" role="img" aria-label="Photograph of lily pads on a pond"></div><div class="news-text"><h3>29 Years and Counting: The Brindle Court Leaders 2014 Women On The Move and Rising Star</h3><p>Houston, TX ~2014 Makes a Stellar Year for the Brindle...</p></div></div>
        <div class="news-item"><div class="thumb pond" role="img" aria-label="Photograph of a tree-lined river"></div><div class="news-text"><h3>29 Years and Counting: The Brindle Court Leaders 2014 Women On The Move and Rising Star</h3><p>Houston, TX ~2014 Makes a Stellar Year for the Brindle...</p></div></div>
        <div class="news-item"><div class="thumb pond" role="img" aria-label="Photograph of a tree-lined river"></div><div class="news-text"><h3>29 Years and Counting: The Brindle Court Leaders 2014 Women On The Move and Rising Star</h3><p>Houston, TX ~2014 Makes a Stellar Year for the Brindle...</p></div></div>
      </div>
    </div>
    <aside class="ad">
      <div class="ad-photo" role="img" aria-label="Advertisement photo of algaecide product containers against blue water"></div>
      <div class="ad-brand">Cleanmarsh Supply</div>
    </aside>
  </div>
</section>

<footer class="site-footer">
  <div class="wrap">
    <div class="quick">
      <h4>Quick Links</h4>
      <ul><li>Home</li><li>About</li><li>Members</li><li>Resources</li><li>Events</li><li>Membership</li><li>Contact</li><li>Advertise with us</li></ul>
    </div>
    <div class="signup">
      <h4>Subscribe to our newsletter !</h4>
      <p>lorem ipsum dollar sit amet, lorem ipsum dollar sit amet, lorem ipsum dollar sit amet, lorem ipsum</p>
      <div class="fields">
        <span class="field half">First Name</span><span class="field half">Last Name</span>
        <span class="field email">Email Id</span>
        <span class="submit"><svg width="22" height="18" viewBox="0 0 22 18"><rect x="1" y="3" width="14" height="14" fill="none" stroke="#0b2674" stroke-width="2"/><path d="M4 9l4 4 12-12" fill="none" stroke="#0b2674" stroke-width="3"/></svg></span>
      </div>
    </div>
    <div class="follow">
      <h4>Follow Us</h4>
      <div class="socials" aria-label="Friendwall, Jobrungo, Clipzora"><i></i><i></i><i></i><i></i></div>
    </div>
  </div>
  <div class="copyright">Copyright © 2014, LONE STAR WETLAND FLORA STEWARDSHIP GUILD. RIGHTS RESERVED.</div>
</footer>

</body>
</html>
```